Business Card Design

I already have a company logo for my company. I have a logo for the manufacturer we represent. I want a professional business card design.

```html
<!DOCTYPE html>
<html lang="en">
<head>
<meta charset="utf-8">
<title>Business Card – Caution Works LLC</title>
<link rel="stylesheet" href="https://fonts.googleapis.com/css2?family=Michroma&family=Lato:wght@400;700&display=swap">
<style>
  :root {
    --backdrop: #2b2b2b;
    --card: #1c1c1c;
    --red: #e0252b;
    --gold: #d4a017;
    --gold-band: #a8820f;
    --text: #e8e8e8;
    --rule: #8a8a8a;
    --silver-light: #e6e6e6;
    --silver-dark: #6f6f6f;
  }
  * { margin: 0; padding: 0; box-sizing: border-box; }
  html, body { width: 1200px; height: 1200px; overflow: hidden; }
  body {
    background: var(--backdrop);
    position: relative;
    font-family: "Lato", sans-serif;
    color: var(--text);
  }
  .card {
    position: absolute;
    left: 201px;
    width: 797px;
    height: 454px;
    background: var(--card);
    overflow: hidden;
  }
  .card-front { top: 96px; }
  .card-back { top: 656px; }

  .person-name {
    position: absolute;
    left: 40px;
    top: 202px;
    font-family: "Michroma", sans-serif;
    font-size: 31px;
    letter-spacing: 1px;
    color: var(--red);
    font-weight: 400;
  }
  .person-title {
    position: absolute;
    left: 40px;
    top: 243px;
    font-size: 22px;
    color: var(--gold);
  }
  .divider {
    position: absolute;
    left: 40px;
    top: 289px;
    width: 713px;
    height: 2px;
    background: linear-gradient(90deg, #555, var(--rule) 40%, #cfcfcf 70%, #e0e0e0);
  }
  .contact-list {
    position: absolute;
    left: 40px;
    top: 313px;
    list-style: none;
    font-size: 21px;
    line-height: 29px;
  }
  .contact-list li { display: flex; align-items: center; gap: 12px; }
  .contact-list svg { width: 17px; height: 17px; flex: none; }

  .company-address {
    position: absolute;
    right: 44px;
    top: 313px;
    text-align: right;
    font-size: 21px;
    line-height: 29px;
    font-style: normal;
  }
  .company-address .company { color: var(--red); }

  .brand {
    position: absolute;
    display: flex;
    flex-direction: column;
    align-items: center;
    text-align: center;
    font-family: "Lato", sans-serif;
    font-weight: 700;
    color: var(--text);
  }
  .brand-mark { background: var(--red); }
  .brand-front { left: 534px; top: 60px; width: 220px; gap: 14px; font-size: 26px; line-height: 30px; }
  .brand-front .brand-mark { width: 56px; height: 56px; }
  .brand-back { left: 178px; top: 90px; width: 440px; gap: 24px; font-size: 48px; line-height: 54px; }
  .brand-back .brand-mark { width: 110px; height: 110px; }

  .bottom-strip { position: absolute; left: 0; top: 408px; width: 797px; height: 46px; }
  .website {
    position: absolute;
    right: 42px;
    top: 420px;
    font-size: 20px;
    letter-spacing: 1px;
    color: #f5f5f5;
  }
</style>
</head>
<body>
  <section class="card card-front">
    <h1 class="person-name">JOHN SMITH</h1>
    <p class="person-title">Founder &amp; CEO</p>

    <div class="brand brand-front">
      <span class="brand-mark"></span>
      <span class="brand-name">CAUTION WORKS<br>LLC</span>
    </div>

    <div class="divider"></div>

    <ul class="contact-list">
      <li>
        <svg viewBox="0 0 24 24" aria-hidden="true"><path fill="var(--red)" d="M6.6 10.8a15 15 0 0 0 6.6 6.6l2.2-2.2a1 1 0 0 1 1-.25 11.4 11.4 0 0 0 3.6.57 1 1 0 0 1 1 1V20a1 1 0 0 1-1 1A17 17 0 0 1 3 4a1 1 0 0 1 1-1h3.5a1 1 0 0 1 1 1c0 1.25.2 2.45.57 3.57a1 1 0 0 1-.25 1z"/></svg>
        (123) 456-7890
      </li>
      <li>
        <svg viewBox="0 0 24 24" aria-hidden="true"><rect x="6" y="2" width="12" height="20" rx="2" fill="none" stroke="var(--red)" stroke-width="2.4"/><circle cx="12" cy="18" r="1.3" fill="var(--red)"/></svg>
        (123) 456-7890
      </li>
      <li>
        <svg viewBox="0 0 24 24" aria-hidden="true"><rect x="2" y="5" width="20" height="14" fill="var(--red)"/><path d="M2 5l10 8 10-8" fill="none" stroke="var(--card)" stroke-width="2"/></svg>
        info@yourwebsitehere.com
      </li>
    </ul>

    <address class="company-address">
      <span class="company">Caution Works LLC</span><br>
      423 Street Address , City<br>
      State &amp; ZIP Code Country
    </address>

    <svg class="bottom-strip" viewBox="0 0 797 46" aria-hidden="true">
      <defs>
        <linearGradient id="silver-bar" x1="0" x2="1" y1="0" y2="0">
          <stop offset="0" stop-color="var(--silver-light)"/>
          <stop offset="0.5" stop-color="var(--silver-dark)"/>
          <stop offset="1" stop-color="#bdbdbd"/>
        </linearGradient>
      </defs>
      <polygon points="0,30 385,30 375,46 0,46" fill="url(#silver-bar)"/>
      <polygon points="392,30 402,30 392,46 382,46" fill="var(--red)"/>
      <polygon points="408,30 418,30 408,46 398,46" fill="var(--red)"/>
      <polygon points="424,30 434,30 424,46 414,46" fill="var(--red)"/>
      <polygon points="440,30 450,30 440,46 430,46" fill="var(--red)"/>
      <polygon points="472,0 797,0 797,46 445,46" fill="var(--gold-band)"/>
    </svg>
    <span class="website">www.yourwebsite.com</span>
  </section>

  <section class="card card-back">
    <div class="brand brand-back">
      <span class="brand-mark"></span>
      <span class="brand-name">CAUTION WORKS<br>LLC</span>
    </div>
  </section>
</body>
</html>
```